Torvane Fabrication, Inc
FYI-I will be out of town March 25th returning late evening Monday the 26th.
I am searching for a vector version of for my logo. So far I cannot find anything. I will keep looking/asking.
Do you have a vector version of your logo separate from your business card?
I have redone my brief. Please read it again.
Please disregard all my other comments below as I have changed the requirements.
8 1/2" x 11" then folded to create a tri-fold is the perfect size.
Thank you for the quick uploads. Also, what paper sizes are you after? The normal 8.5 x 11? or a bespoke size.
Kind regards
Sorry everyone, I realized I did not give you much to go on. I guess I got anxious to quick. When I put more thought into it, this is what I came up with. Hopefully you guys can dress it up a little bit to make it look professional. I will upload my logo as soon as I receive from printer. Hopefully, this should be a much better place to start.
Hello Sir,
Could you please upload you logo.

```html
<!DOCTYPE html>
<html lang="en">
<head>
<meta charset="utf-8">
<title>Torvane Fabrication, Inc – Tri-fold Brochure</title>
<link href="https://fonts.googleapis.com/css2?family=Arimo:wght@400;700&display=swap" rel="stylesheet">
<style>
  :root {
    --stage: #e9e6e1;
    --paper: #ffffff;
    --blue: #1b82d4;
    --blue-deep: #0a5aa8;
    --blue-light: #5fb0ea;
    --sky: #dcebf7;
    --mist: #eef2f6;
    --ink: #3d4650;
    --ink-soft: #6b7682;
    --bullet: #e2604f;
  }
  * { box-sizing: border-box; margin: 0; padding: 0; }
  html, body { width: 1200px; height: 847px; overflow: hidden; }
  body { background: var(--stage); font-family: "Arimo", Arial, sans-serif; color: var(--ink); position: relative; }

  .panel { position: absolute; top: 74px; width: 490px; height: 700px; background: var(--paper); overflow: hidden; box-shadow: 0 4px 14px rgba(0,0,0,.18); }
  .panel--cover { left: 80px; }
  .panel--inside { left: 630px; }

  /* Cover panel */
  .cover-art { position: absolute; inset: 0; background: linear-gradient(160deg, #f7f9fb 0%, #e3e9ef 35%, #f4f6f8 55%, #dfe6ed 80%, #f5f7f9 100%); }
  .fold-line { position: absolute; left: 0; right: 0; top: 350px; border-top: 1px dashed rgba(10,90,168,.15); }

  .flap { position: absolute; left: 0; top: 0; width: 490px; height: 350px; transform: rotate(180deg); display: flex; flex-direction: column; align-items: center; padding-top: 60px; }
  .badge-circle { width: 46px; height: 46px; border-radius: 50%; background: radial-gradient(circle at 40% 35%, var(--blue-light), var(--blue-deep)); color: #fff; font-weight: 700; font-size: 28px; display: flex; align-items: center; justify-content: center; box-shadow: 0 0 0 3px rgba(27,130,212,.18); }
  .flap-line { font-size: 13px; color: var(--blue-deep); margin: 10px 0 14px; }
  .contact-box { margin-top: 16px; width: 150px; background: var(--blue); color: #fff; font-size: 7px; line-height: 1.45; padding: 7px 10px; }
  .contact-box strong { font-size: 8px; }

  .brand { position: absolute; left: 38px; top: 382px; }
  .brand-name { display: flex; align-items: center; gap: 10px; font-weight: 700; font-size: 22px; color: var(--blue-deep); }
  .brand-dot { width: 34px; height: 34px; border-radius: 50%; background: var(--blue-deep); }
  .brand-tagline { margin-top: 8px; font-size: 7px; letter-spacing: .04em; color: var(--ink-soft); line-height: 1.5; }

  .cover-wave { position: absolute; left: 0; bottom: 0; width: 490px; height: 170px; }
  .cover-message { position: absolute; left: 40px; right: 40px; bottom: 36px; text-align: center; color: #fff; font-size: 11px; line-height: 1.5; }
  .cover-url { position: absolute; left: 0; right: 0; bottom: 14px; text-align: center; color: #fff; font-size: 7px; }

  /* Inside panel */
  .band-top { position: absolute; left: 0; top: 0; width: 490px; height: 82px; }
  .section-title { position: absolute; left: 24px; color: #fff; font-weight: 700; font-size: 22px; letter-spacing: .01em; }
  .section-title--offer { top: 16px; }
  .offer-bg { position: absolute; left: 0; top: 60px; width: 490px; height: 270px; background: linear-gradient(180deg, #ffffff 0%, var(--mist) 100%); }
  .offer-list { position: absolute; left: 44px; top: 108px; right: 40px; list-style: none; }
  .offer-list li { display: flex; align-items: flex-start; gap: 12px; font-size: 10px; line-height: 1.35; margin-bottom: 14px; color: var(--ink); }
  .num { flex: 0 0 20px; height: 20px; border-radius: 50%; background: var(--blue); color: #fff; font-size: 10px; font-weight: 700; display: flex; align-items: center; justify-content: center; margin-top: -3px; }

  .band-mid { position: absolute; left: 0; top: 318px; width: 490px; height: 90px; }
  .section-title--highlights { top: 346px; }

  .note-box { position: absolute; left: 24px; top: 440px; width: 140px; height: 170px; background: var(--mist); padding: 18px 12px; text-align: center; }
  .note-box .badge-circle { margin: 0 auto 14px; }
  .note-text { font-size: 7.5px; line-height: 1.5; color: var(--ink-soft); }

  .highlight-list { position: absolute; left: 186px; top: 418px; right: 20px; list-style: none; }
  .highlight-list li { position: relative; padding-left: 14px; font-size: 8.5px; line-height: 1.35; margin-bottom: 9px; color: var(--ink); }
  .highlight-list li::before { content: ""; position: absolute; left: 0; top: 3px; width: 6px; height: 6px; border-radius: 50%; background: var(--bullet); }
</style>
</head>
<body>

<section class="panel panel--cover">
  <div class="cover-art" role="img" aria-label="Soft grey background of large machine gears"></div>
  <div class="fold-line"></div>

  <div class="flap">
    <div class="badge-circle">?</div>
    <p class="flap-line">Are We a Fit for Your Company?</p>
    <div class="badge-circle">i</div>
    <p class="flap-line">It's Certainly Worth the Conversation!</p>
    <div class="contact-box">
      <strong>Torvane Fabrication, Inc</strong><br>
      2280 Larch Road, Suite 4<br>
      Dalton, OH 44618<br>
      Tel: 555-0142<br>
      Fax: 555-0143<br>
      info@torvanefab.com
    </div>
  </div>

  <div class="brand">
    <div class="brand-name"><span class="brand-dot"></span>Torvane Fabrication, Inc</div>
    <p class="brand-tagline">PROFESSIONAL PARTS AND SOLUTIONS SINCE 1987<br>FOR MANUFACTURING AND PACKAGING</p>
  </div>

  <svg class="cover-wave" viewBox="0 0 490 170" preserveAspectRatio="none" aria-hidden="true">
    <defs>
      <linearGradient id="coverBlue" x1="0" y1="0" x2="0" y2="1">
        <stop offset="0" stop-color="#4aa6ea"/>
        <stop offset="1" stop-color="#0a5aa8"/>
      </linearGradient>
    </defs>
    <path d="M0 40 C120 10 300 70 490 25 L490 170 L0 170 Z" fill="#bcdaf3" opacity=".7"/>
    <path d="M0 58 C140 28 320 86 490 44 L490 170 L0 170 Z" fill="url(#coverBlue)"/>
  </svg>
  <p class="cover-message">Our ONLY objective as manufacturers representatives, is to meet or exceed your expectations and challenges, each and every time you trust us with your valued business.</p>
  <p class="cover-url">www.torvanefab.com</p>
</section>

<section class="panel panel--inside">
  <div class="offer-bg"></div>
  <svg class="band-top" viewBox="0 0 490 82" preserveAspectRatio="none" aria-hidden="true">
    <defs>
      <linearGradient id="topBlue" x1="0" y1="0" x2="1" y2="0">
        <stop offset="0" stop-color="#0a5aa8"/>
        <stop offset="1" stop-color="#3b9de6"/>
      </linearGradient>
    </defs>
    <path d="M0 0 H490 V58 C360 82 170 40 0 66 Z" fill="url(#topBlue)"/>
    <path d="M0 66 C170 40 360 82 490 58 V64 C360 88 170 48 0 72 Z" fill="#9ccbf0" opacity=".7"/>
  </svg>
  <h2 class="section-title section-title--offer">WHAT WE OFFER:</h2>

  <ol class="offer-list">
    <li><span class="num">1</span>Finding solutions, providing excellent parts and service for the following commodities since 1987</li>
    <li><span class="num">2</span>Metal Stamping- Kessler Metal Stamping</li>
    <li><span class="num">3</span>Machining-CNC Precision</li>
    <li><span class="num">4</span>Sheet Metal Fabrication- Ironline Works</li>
    <li><span class="num">5</span>Packaging- Halvorsen Packaging</li>
  </ol>

  <svg class="band-mid" viewBox="0 0 490 90" preserveAspectRatio="none" aria-hidden="true">
    <defs>
      <linearGradient id="midBlue" x1="0" y1="0" x2="1" y2="0">
        <stop offset="0" stop-color="#0a5aa8"/>
        <stop offset="1" stop-color="#3b9de6"/>
      </linearGradient>
    </defs>
    <path d="M0 14 C150 -4 330 30 490 8 V16 C330 38 150 6 0 22 Z" fill="#9ccbf0" opacity=".7"/>
    <path d="M0 22 C150 6 330 38 490 16 V70 C340 92 160 54 0 78 Z" fill="url(#midBlue)"/>
  </svg>
  <h2 class="section-title section-title--highlights">HIGHLIGHTS:</h2>

  <div class="note-box">
    <div class="badge-circle">!</div>
    <p class="note-text">We recently added a cable and harness assembly &amp; distribution center locally in Dalton</p>
  </div>

  <ul class="highlight-list">
    <li>Controlled Inventory</li>
    <li>Experts at Scheduled Deliveries</li>
    <li>Costs Reduction: Our buying power lowers your prices</li>
    <li>Program Managers to meet your Specific communication Requirements</li>
    <li>ISO9100 Certified CNC Machining</li>
    <li>Servicing All Industries with Precision Products</li>
    <li>Proto-Type to Production - Engineering assistance available on site</li>
    <li>My personal guarantee: We truly don't rest until your challenges are met.</li>
  </ul>
</section>

</body>
</html>
```